Technology Services Fleet Wrap

We provide IT and Network Management Services to small to medium sized businesses. We would like to have our website, phone number, logo, services listed. We have a business to wrap the car but we need the design file for him to print the vinyl. Included an example picture of something we like. The blue in our logo is a color we would like to keep. The logo can be all one color it does not have to have the tech background that is currently in it

Target Market(s)

Businesses

Industry/Entity Type

Information Technology

```html
<!DOCTYPE html>
<html lang="en">
<head>
<meta charset="utf-8">
<title>Halcyon Tech — Fleet Wrap Layout</title>
<link rel="stylesheet" href="https://fonts.googleapis.com/css2?family=Oswald:wght@300;400;600;700&display=swap">
<style>
  :root {
    --backdrop: #5b5b5b;
    --vinyl-white: #ffffff;
    --brand-blue: #2f8fe4;
    --brand-blue-deep: #2462b8;
    --rear-blue: #2f4fb0;
    --rear-blue-light: #3a5fc6;
    --navy: #171a33;
    --accent-text: #3d9cf2;
  }
  html, body {
    margin: 0;
    padding: 0;
    width: 932px;
    height: 1200px;
    overflow: hidden;
    background: var(--backdrop);
  }
  .wrap-sheet {
    display: block;
    width: 932px;
    height: 1200px;
  }
  .van-body { fill: var(--vinyl-white); }
  .window-cutout { fill: var(--backdrop); }
  .stripe-navy { fill: var(--navy); }
  .service-bar { fill: var(--navy); }
  .service-cap { fill: var(--brand-blue); }
  .service-text {
    font-family: "Oswald", sans-serif;
    font-weight: 400;
    font-size: 20px;
    fill: var(--vinyl-white);
  }
  .service-text .highlight { fill: var(--accent-text); font-weight: 600; }
  .brand-name {
    font-family: "Oswald", sans-serif;
    font-weight: 300;
    font-size: 34px;
    fill: var(--vinyl-white);
  }
  .brand-name.small { font-size: 22px; }
  .brand-ring { fill: none; stroke: var(--vinyl-white); stroke-width: 3; }
  .social-dot { fill: var(--vinyl-white); }
  .phone-pill { fill: var(--navy); }
  .phone-text {
    font-family: "Oswald", sans-serif;
    font-weight: 600;
    font-size: 36px;
    fill: var(--vinyl-white);
  }
  .phone-text.small { font-size: 29px; }
  .phone-text .dash { fill: var(--accent-text); }
  .web-text {
    font-family: "Oswald", sans-serif;
    font-weight: 700;
    font-size: 24px;
    fill: var(--navy);
  }
  .web-text .tld { fill: var(--brand-blue); font-weight: 300; }
  .web-text.on-blue { fill: var(--vinyl-white); }
  .web-text.on-blue .tld { fill: var(--vinyl-white); }
  .badge-shield { fill: var(--navy); }
  .badge-seal { fill: #8fc4ec; stroke: #c9ccd2; stroke-width: 3; }
  .rocker-white { fill: var(--vinyl-white); }
</style>
</head>
<body>
<svg class="wrap-sheet" viewBox="20 596 1660 2138" preserveAspectRatio="xMidYMid meet" xmlns="http://www.w3.org/2000/svg">
  <defs>
    <linearGradient id="blue-field" x1="0" y1="0" x2="1" y2="0.3">
      <stop offset="0" stop-color="var(--brand-blue-deep)"/>
      <stop offset="1" stop-color="var(--brand-blue)"/>
    </linearGradient>
    <linearGradient id="rear-field" x1="0" y1="0" x2="1" y2="1">
      <stop offset="0" stop-color="var(--rear-blue)"/>
      <stop offset="1" stop-color="var(--rear-blue-light)"/>
    </linearGradient>
    <clipPath id="van-side-clip">
      <path d="M40,1195 L380,1192 L870,1212 Q930,1230 960,1285 L1140,1390 Q1240,1430 1262,1480 L1272,1557 L1175,1557 Q1150,1515 1085,1512 Q1015,1515 990,1557 L330,1557 Q305,1520 245,1518 Q185,1520 165,1557 L65,1557 L65,1440 L35,1420 Z"/>
    </clipPath>
  </defs>

  <!-- Driver side panel -->
  <g class="side-panel driver-side">
    <g class="side-artwork" clip-path="url(#van-side-clip)">
      <path class="van-body" d="M40,1195 L380,1192 L870,1212 Q930,1230 960,1285 L1140,1390 Q1240,1430 1262,1480 L1272,1557 L1175,1557 Q1150,1515 1085,1512 Q1015,1515 990,1557 L330,1557 Q305,1520 245,1518 Q185,1520 165,1557 L65,1557 L65,1440 L35,1420 Z"/>
      <polygon role="img" aria-label="Blue circuit-board pattern field" fill="url(#blue-field)" points="20,1180 355,1180 505,1570 20,1570"/>
      <polygon class="stripe-navy" points="355,1180 373,1180 524,1570 506,1570"/>
      <polygon class="stripe-navy" points="386,1180 402,1180 556,1570 540,1570"/>
    </g>
    <path class="window-cutout" d="M830,1295 L950,1293 Q1000,1300 1060,1350 L1150,1440 Q1168,1468 1145,1470 L870,1440 Q830,1432 825,1400 Z"/>
  </g>

  <g class="service-list driver-side">
    <rect class="service-cap" x="405" y="1218" width="362" height="30" rx="15"/>
    <rect class="service-bar" x="405" y="1218" width="352" height="30" rx="4"/>
    <text class="service-text" x="442" y="1242">VoIP <tspan class="highlight">Solutions</tspan></text>
    <rect class="service-cap" x="428" y="1253" width="339" height="30" rx="15"/>
    <rect class="service-bar" x="428" y="1253" width="329" height="30" rx="4"/>
    <text class="service-text" x="456" y="1277"><tspan class="highlight">Support From</tspan> AnyWhere</text>
    <rect class="service-cap" x="448" y="1288" width="319" height="30" rx="15"/>
    <rect class="service-bar" x="448" y="1288" width="309" height="30" rx="4"/>
    <text class="service-text" x="475" y="1312">Data <tspan class="highlight">Protection</tspan></text>
    <rect class="service-cap" x="466" y="1323" width="301" height="30" rx="15"/>
    <rect class="service-bar" x="466" y="1323" width="291" height="30" rx="4"/>
    <text class="service-text" x="494" y="1347"><tspan class="highlight">Network Security</tspan> &amp; Audits</text>
    <rect class="service-cap" x="482" y="1358" width="285" height="30" rx="15"/>
    <rect class="service-bar" x="482" y="1358" width="275" height="30" rx="4"/>
    <text class="service-text" x="509" y="1382">Network <tspan class="highlight">Management</tspan></text>
    <rect class="service-cap" x="498" y="1393" width="269" height="30" rx="15"/>
    <rect class="service-bar" x="498" y="1393" width="259" height="30" rx="4"/>
    <text class="service-text" x="523" y="1417"><tspan class="highlight">Web Design</tspan> &amp; SEO</text>
  </g>

  <g class="brand-block driver-side">
    <circle class="social-dot" cx="88" cy="1237" r="13"/>
    <circle class="social-dot" cx="121" cy="1237" r="13"/>
    <circle class="social-dot" cx="155" cy="1237" r="13"/>
    <circle class="brand-ring" cx="262" cy="1350" r="100"/>
    <text class="brand-name" x="138" y="1520" textLength="244" lengthAdjust="spacing">HALCYON TECH</text>
  </g>

  <g class="credentials driver-side">
    <polygon class="badge-shield" points="555,1443 605,1443 610,1480 580,1505 550,1480"/>
    <circle class="badge-seal" cx="665" cy="1472" r="32"/>
    <text class="web-text" x="566" y="1538" textLength="152" lengthAdjust="spacingAndGlyphs">HalcyonTech<tspan class="tld">.com</tspan></text>
  </g>

  <g class="phone driver-side">
    <rect class="phone-pill" x="857" y="1480" width="218" height="48" rx="24"/>
    <text class="phone-text" x="868" y="1517" textLength="196" lengthAdjust="spacingAndGlyphs">555<tspan class="dash">-</tspan>014<tspan class="dash">-</tspan>2290</text>
  </g>

  <g class="rocker-strip driver-side">
    <polygon class="rocker-white" points="590,1615 968,1615 968,1643 590,1643"/>
    <polygon fill="var(--brand-blue)" points="362,1612 540,1612 552,1643 362,1643"/>
    <polygon class="stripe-navy" points="540,1612 555,1612 568,1643 553,1643"/>
    <polygon class="stripe-navy" points="566,1612 580,1612 593,1643 579,1643"/>
  </g>

  <!-- Passenger side panel -->
  <g class="side-panel passenger-side" transform="translate(1307,490) scale(-1,1)">
    <g class="side-artwork" clip-path="url(#van-side-clip)">
      <path class="van-body" d="M40,1195 L380,1192 L870,1212 Q930,1230 960,1285 L1140,1390 Q1240,1430 1262,1480 L1272,1557 L1175,1557 Q1150,1515 1085,1512 Q1015,1515 990,1557 L330,1557 Q305,1520 245,1518 Q185,1520 165,1557 L65,1557 L65,1440 L35,1420 Z"/>
      <polygon role="img" aria-label="Blue circuit-board pattern field" fill="url(#blue-field)" points="20,1180 355,1180 505,1570 20,1570"/>
      <polygon class="stripe-navy" points="355,1180 373,1180 524,1570 506,1570"/>
      <polygon class="stripe-navy" points="386,1180 402,1180 556,1570 540,1570"/>
    </g>
    <path class="window-cutout" d="M830,1295 L950,1293 Q1000,1300 1060,1350 L1150,1440 Q1168,1468 1145,1470 L870,1440 Q830,1432 825,1400 Z"/>
  </g>

  <g class="service-list passenger-side">
    <rect class="service-cap" x="541" y="1708" width="362" height="30" rx="15"/>
    <rect class="service-bar" x="551" y="1708" width="352" height="30" rx="4"/>
    <text class="service-text" x="868" y="1732" text-anchor="end">VoIP <tspan class="highlight">Solutions</tspan></text>
    <rect class="service-cap" x="541" y="1743" width="347" height="30" rx="15"/>
    <rect class="service-bar" x="551" y="1743" width="337" height="30" rx="4"/>
    <text class="service-text" x="852" y="1767" text-anchor="end"><tspan class="highlight">Support From</tspan> AnyWhere</text>
    <rect class="service-cap" x="541" y="1778" width="331" height="30" rx="15"/>
    <rect class="service-bar" x="551" y="1778" width="321" height="30" rx="4"/>
    <text class="service-text" x="834" y="1802" text-anchor="end">Data <tspan class="highlight">Protection</tspan></text>
    <rect class="service-cap" x="541" y="1813" width="315" height="30" rx="15"/>
    <rect class="service-bar" x="551" y="1813" width="305" height="30" rx="4"/>
    <text class="service-text" x="817" y="1837" text-anchor="end"><tspan class="highlight">Network Security</tspan> &amp; Audits</text>
    <rect class="service-cap" x="541" y="1848" width="299" height="30" rx="15"/>
    <rect class="service-bar" x="551" y="1848" width="289" height="30" rx="4"/>
    <text class="service-text" x="800" y="1872" text-anchor="end">Network <tspan class="highlight">Management</tspan></text>
    <rect class="service-cap" x="541" y="1883" width="283" height="30" rx="15"/>
    <rect class="service-bar" x="551" y="1883" width="273" height="30" rx="4"/>
    <text class="service-text" x="785" y="1907" text-anchor="end"><tspan class="highlight">Web Design</tspan> &amp; SEO</text>
  </g>

  <g class="brand-block passenger-side">
    <circle class="social-dot" cx="1152" cy="1720" r="13"/>
    <circle class="social-dot" cx="1185" cy="1720" r="13"/>
    <circle class="social-dot" cx="1218" cy="1720" r="13"/>
    <circle class="brand-ring" cx="1042" cy="1840" r="100"/>
    <text class="brand-name" x="920" y="2010" textLength="245" lengthAdjust="spacing">HALCYON TECH</text>
  </g>

  <g class="credentials passenger-side">
    <polygon class="badge-shield" points="615,1932 665,1932 670,1969 640,1994 610,1969"/>
    <circle class="badge-seal" cx="725" cy="1961" r="32"/>
    <text class="web-text" x="590" y="2028" textLength="152" lengthAdjust="spacingAndGlyphs">HalcyonTech<tspan class="tld">.com</tspan></text>
  </g>

  <g class="phone passenger-side">
    <rect class="phone-pill" x="232" y="1970" width="218" height="48" rx="24"/>
    <text class="phone-text" x="244" y="2007" textLength="194" lengthAdjust="spacingAndGlyphs">555<tspan class="dash">-</tspan>014<tspan class="dash">-</tspan>2290</text>
  </g>

  <g class="rocker-strip passenger-side">
    <polygon class="rocker-white" points="340,2105 722,2105 712,2132 340,2132"/>
    <polygon class="stripe-navy" points="728,2105 742,2105 731,2132 717,2132"/>
    <polygon class="stripe-navy" points="752,2105 766,2105 755,2132 741,2132"/>
    <polygon fill="var(--brand-blue)" points="772,2105 945,2105 945,2132 761,2132"/>
  </g>

  <!-- Rear doors -->
  <g class="rear-panel">
    <path role="img" aria-label="Blue circuit-board pattern field on rear doors" fill="url(#rear-field)" d="M1330,1462 L1425,1462 Q1430,1478 1445,1478 L1535,1478 Q1552,1478 1555,1462 L1655,1465 Q1668,1580 1670,1690 L1648,1700 L1648,1812 L1330,1812 L1330,1700 L1310,1690 Q1312,1580 1330,1462 Z"/>
    <circle class="brand-ring" cx="1490" cy="1572" r="66"/>
    <text class="brand-name small" x="1411" y="1678" textLength="158" lengthAdjust="spacing">HALCYON TECH</text>
    <rect class="phone-pill" x="1398" y="1686" width="182" height="42" rx="21"/>
    <text class="phone-text small" x="1409" y="1718" textLength="160" lengthAdjust="spacingAndGlyphs">555<tspan class="dash">-</tspan>014<tspan class="dash">-</tspan>2290</text>
    <text class="web-text on-blue" x="1398" y="1800" textLength="152" lengthAdjust="spacingAndGlyphs">HalcyonTech<tspan class="tld">.com</tspan></text>
  </g>
</svg>
</body>
</html>
```